Lakeshore Vision Associates, P.C.
Diseases and Surgeries of the Retina, Macula and Vitreous
Lakeshore Vision Associates, P.C. - Medical
Creative Brief
Professional
Peter R. Haldane, MD
Birchwood Medical Tower 4215 N. Lindon Suite 812 Wexmore, IL 60952
peter@lakeshorevsa.com
www.lakeshorevsa.com
Appointment Date: MM/DD/YYYY at ____________am ___________pm Please telephone in advance if you will be unable to keep the appointment

```html
<!DOCTYPE html>
<html lang="en">
<head>
<meta charset="utf-8">
<title>Lakeshore Vision Associates – Stationery</title>
<link href="https://fonts.googleapis.com/css2?family=Open+Sans:wght@400;600&display=swap" rel="stylesheet">
<style>
  :root{
    --stage:#e9e6e2;
    --paper:#ffffff;
    --ink:#4a4a4a;
    --ink-soft:#8a8a8a;
    --orange:#e8621c;
    --orange-deep:#c23a12;
    --orange-light:#f59a3e;
    --rule:#9a9a9a;
  }
  *{box-sizing:border-box;margin:0;padding:0}
  html,body{width:1200px;height:715px;overflow:hidden}
  body{background:var(--stage);font-family:"Open Sans",Arial,sans-serif;color:var(--ink);position:relative}
  .sheet{position:absolute;background:var(--paper);box-shadow:0 3px 10px rgba(0,0,0,.25);overflow:hidden}

  .wordmark{display:flex;align-items:center;gap:6px}
  .wordmark .dot{border-radius:50%;background:var(--orange);flex:none}
  .wordmark .name{font-weight:600;text-transform:uppercase;letter-spacing:.12em;color:var(--ink);line-height:1.2}
  .wordmark.light .name{color:#fff}
  .wordmark.light .dot{background:#fff}

  .swoosh{position:absolute;left:0;bottom:0;width:100%}

  /* left card stack */
  .card-plain{left:72px;top:144px;width:211px;height:139px;border-radius:8px}
  .card-orange{left:72px;width:211px;height:139px;border-radius:8px;
    background:radial-gradient(circle at 30% 40%,var(--orange-light),var(--orange) 45%,var(--orange-deep) 100%)}
  .card-orange.first{top:300px}
  .card-orange.second{top:427px}
  .card-plain .wordmark,.card-orange .wordmark{position:absolute;right:14px;top:58px}
  .card-plain .name,.card-orange .name{font-size:6px;max-width:80px}
  .card-plain .dot,.card-orange .dot{width:14px;height:14px}
  .card-orange .web{position:absolute;right:14px;top:80px;font-size:5px;color:#fff}

  /* letterhead */
  .letterhead{left:324px;top:84px;width:372px;height:600px}
  .letterhead .wordmark{position:absolute;left:22px;top:22px}
  .letterhead .dot{width:22px;height:22px}
  .letterhead .name{font-size:9px;max-width:120px}
  .letterhead .address{position:absolute;right:22px;top:22px;font-size:6px;line-height:1.5;color:var(--ink-soft);text-align:left}
  .letterhead .footer-band{position:absolute;left:0;bottom:0;width:100%;height:18px;background:var(--orange-deep)}
  .letterhead .footer-band span{position:absolute;left:18px;top:4px;font-size:6.5px;color:#fff;letter-spacing:.05em}

  /* envelopes */
  .envelope-back{left:744px;top:84px;width:408px;height:130px;border-radius:2px}
  .envelope-back .flap{position:absolute;left:0;top:0;width:100%;height:80px}
  .envelope-back .seal{position:absolute;left:194px;top:50px;width:20px;height:20px;border-radius:50%;background:#fff}
  .envelope-open{left:726px;top:168px;width:408px;height:100px;border-radius:2px}
  .envelope-open .flap{position:absolute;left:0;top:0;width:100%;height:100px}
  .envelope-open .seal{position:absolute;left:194px;top:64px;width:18px;height:18px;border-radius:50%;background:var(--orange)}
  .envelope-front{left:716px;top:248px;width:420px;height:150px;border-radius:2px}
  .envelope-front .wordmark{position:absolute;left:20px;top:20px}
  .envelope-front .dot{width:20px;height:20px}
  .envelope-front .name{font-size:8px;max-width:110px}
  .envelope-front .return{position:absolute;left:46px;top:54px;font-size:5.5px;line-height:1.5;color:var(--ink-soft)}

  /* business cards */
  .biz{top:456px;width:213px;height:122px;border-radius:3px}
  .biz.front{left:680px}
  .biz.back{left:907px}
  .biz .wordmark{position:absolute;left:12px;top:28px}
  .biz .dot{width:18px;height:18px}
  .biz .name{font-size:7px;max-width:70px}
  .biz .contact{position:absolute;top:14px;font-size:5.5px;line-height:1.55;color:var(--ink-soft)}
  .biz.front .contact{left:108px}
  .biz.back .contact{left:16px}
  .biz .contact .person{color:var(--orange);font-weight:600;font-size:7px;display:block;margin-bottom:2px}
  .biz.back .side{position:absolute;left:118px;top:30px;font-size:5.5px;line-height:1.55;color:var(--ink-soft)}
</style>
</head>
<body>

<svg width="0" height="0" style="position:absolute">
  <defs>
    <linearGradient id="band" x1="0" x2="1">
      <stop offset="0" stop-color="#c23a12"/>
      <stop offset=".6" stop-color="#e8621c"/>
      <stop offset="1" stop-color="#f59a3e"/>
    </linearGradient>
    <linearGradient id="flapFill" x1="0" x2="1">
      <stop offset="0" stop-color="#c23a12"/>
      <stop offset=".5" stop-color="#f07a28"/>
      <stop offset="1" stop-color="#c23a12"/>
    </linearGradient>
  </defs>
</svg>

<!-- left card stack -->
<div class="sheet card-plain">
  <div class="wordmark"><span class="name">Lakeshore Vision Associates</span><span class="dot"></span></div>
</div>
<div class="sheet card-orange first">
  <div class="wordmark light"><span class="name">Lakeshore Vision Associates</span><span class="dot"></span></div>
  <div class="web">www.lakeshorevsa.com</div>
</div>
<div class="sheet card-orange second">
  <div class="wordmark light"><span class="name">Lakeshore Vision Associates</span><span class="dot"></span></div>
  <div class="web">www.lakeshorevsa.com</div>
</div>

<!-- letterhead -->
<div class="sheet letterhead">
  <div class="wordmark"><span class="dot"></span><span class="name">Lakeshore Vision Associates</span></div>
  <div class="address">
    Birchwood Medical Tower<br>
    4215 N. Lindon Suite 812<br>
    Wexmore, IL 60952<br>
    T 312.555.0148<br>
    F 312.555.0149<br>
    www.lakeshorevsa.com
  </div>
  <svg class="swoosh" viewBox="0 0 372 40" preserveAspectRatio="none" height="40" style="bottom:18px">
    <path d="M0 34 Q180 8 372 26" fill="none" stroke="#9a9a9a" stroke-width="1.5"/>
    <path d="M0 40 Q190 18 372 30 L372 40 Z" fill="url(#band)"/>
  </svg>
  <div class="footer-band"><span>www.lakeshorevsa.com</span></div>
</div>

<!-- envelopes -->
<div class="sheet envelope-back">
  <svg class="flap" viewBox="0 0 408 80" preserveAspectRatio="none">
    <path d="M0 0 H408 V20 L204 70 L0 20 Z" fill="url(#flapFill)"/>
  </svg>
  <div class="seal"></div>
</div>
<div class="sheet envelope-open">
  <svg class="flap" viewBox="0 0 408 100" preserveAspectRatio="none">
    <path d="M0 0 L204 78 L408 0" fill="none" stroke="#d0d0d0" stroke-width="1.2"/>
  </svg>
  <div class="seal"></div>
</div>
<div class="sheet envelope-front">
  <div class="wordmark"><span class="dot"></span><span class="name">Lakeshore Vision Associates</span></div>
  <div class="return">Birchwood Medical Tower · 4215 N. Lindon Suite 812 · Wexmore, IL 60952</div>
  <svg class="swoosh" viewBox="0 0 420 36" preserveAspectRatio="none" height="36">
    <path d="M0 14 Q200 2 420 12" fill="none" stroke="#9a9a9a" stroke-width="1.5"/>
    <path d="M0 20 Q210 6 420 18 L420 36 L0 36 Z" fill="url(#band)"/>
  </svg>
</div>

<!-- business cards -->
<div class="sheet biz front">
  <div class="wordmark"><span class="dot"></span><span class="name">Lakeshore Vision Associates</span></div>
  <div class="contact">
    <span class="person">Peter R. Haldane, MD</span>
    Birchwood Medical Tower<br>
    4215 N. Lindon Suite 812<br>
    Wexmore, IL 60952<br>
    T 312.555.0148<br>
    peter@lakeshorevsa.com
  </div>
  <svg class="swoosh" viewBox="0 0 213 26" preserveAspectRatio="none" height="26">
    <path d="M0 10 Q100 0 213 8" fill="none" stroke="#9a9a9a" stroke-width="1.2"/>
    <path d="M0 16 Q110 4 213 12 L213 26 L0 26 Z" fill="url(#band)"/>
  </svg>
</div>
<div class="sheet biz back">
  <div class="contact">
    <span class="person">Peter R. Haldane, MD</span>
    Retina, Macula and Vitreous
  </div>
  <div class="side">
    Birchwood Medical Tower<br>
    4215 N. Lindon Suite 812<br>
    Wexmore, IL 60952<br>
    T 312.555.0148<br>
    www.lakeshorevsa.com
  </div>
  <svg class="swoosh" viewBox="0 0 213 26" preserveAspectRatio="none" height="26">
    <path d="M0 10 Q100 0 213 8" fill="none" stroke="#9a9a9a" stroke-width="1.2"/>
    <path d="M0 16 Q110 4 213 12 L213 26 L0 26 Z" fill="url(#band)"/>
  </svg>
</div>

</body>
</html>
```